brisknest

i want to ues this logo and the same colors used on the business card

cleaning & service

Industry/Entity Type

Business

Contact Information for Business Card

Font styles to use
Serif
Sans Serif
Decorative
Script

Colors
add136
0692cd
000000
5c5c5c
fbfbfb

Requirements
Must have
• cleaning things

```html
<!DOCTYPE html>
<html lang="en">
<head>
<meta charset="utf-8">
<title>Brisknest – Business Card</title>
<link rel="stylesheet" href="https://fonts.googleapis.com/css2?family=Open+Sans:wght@400;600;700&display=swap">
<style>
  :root {
    --green: #add136;
    --blue: #0692cd;
    --blue-deep: #0a6fb5;
    --ink: #000000;
    --grey: #5c5c5c;
    --paper: #fbfbfb;
    --backdrop: #e9e9e9;
  }
  * { margin: 0; padding: 0; box-sizing: border-box; }
  html, body {
    width: 1200px; height: 900px; overflow: hidden;
    background: var(--backdrop);
    font-family: "Open Sans", Arial, sans-serif;
  }
  .stage {
    position: relative; width: 1200px; height: 900px;
  }
  .card {
    position: absolute; left: 300px;
    width: 600px; height: 343px;
    background: var(--paper);
    box-shadow: 0 4px 14px rgba(0,0,0,.18);
    overflow: hidden;
  }
  .card--back { top: 90px; }
  .card--front { top: 470px; }

  .wordmark {
    position: absolute;
    display: flex; align-items: center; gap: 10px;
    font-weight: 700; color: var(--blue-deep);
    letter-spacing: .5px;
  }
  .wordmark__square {
    width: 22px; height: 22px; background: var(--green);
  }
  .card--back .wordmark {
    left: 50%; top: 50%; transform: translate(-50%, -50%);
    font-size: 40px;
  }
  .card--front .wordmark {
    left: 360px; top: 140px; font-size: 36px;
  }

  .card__art { position: absolute; left: 0; top: 0; }

  .holder {
    position: absolute; left: 66px; top: 22px; line-height: 1.15;
  }
  .holder__name { font-size: 21px; font-weight: 700; color: var(--blue-deep); }
  .holder__role { font-size: 15px; color: var(--ink); }

  .contact {
    position: absolute; left: 20px; top: 198px;
    list-style: none; font-size: 16px; color: var(--ink);
  }
  .contact__item { display: flex; align-items: center; gap: 10px; height: 24px; }
  .contact__icon { width: 12px; height: 12px; fill: var(--blue-deep); flex: none; }
</style>
</head>
<body>
<main class="stage">

  <section class="card card--back" aria-label="Card back">
    <div class="wordmark"><span class="wordmark__square"></span>Brisknest</div>
  </section>

  <section class="card card--front" aria-label="Card front">
    <svg class="card__art" width="600" height="343" viewBox="0 0 600 343" aria-hidden="true">
      <polygon points="0,18 26,18 0,40" fill="var(--green)"/>
      <polygon points="30,18 58,18 58,58 0,58" fill="var(--blue-deep)"/>
      <polygon points="0,258 300,258 284,282 0,282" fill="var(--green)"/>
      <polygon points="306,270 600,270 600,343 276,343" fill="var(--blue-deep)"/>
    </svg>

    <div class="holder">
      <div class="holder__name">Mark Ellison</div>
      <div class="holder__role">Managing Director</div>
    </div>

    <ul class="contact">
      <li class="contact__item">
        <svg class="contact__icon" viewBox="0 0 24 24"><path d="M6.6 10.8a15.1 15.1 0 0 0 6.6 6.6l2.2-2.2a1 1 0 0 1 1-.25 11.4 11.4 0 0 0 3.6.57 1 1 0 0 1 1 1V20a1 1 0 0 1-1 1A17 17 0 0 1 3 4a1 1 0 0 1 1-1h3.5a1 1 0 0 1 1 1c0 1.25.2 2.45.57 3.57a1 1 0 0 1-.25 1z"/></svg>
        (044)-318-2645
      </li>
      <li class="contact__item">
        <svg class="contact__icon" viewBox="0 0 24 24"><path d="M2 5h20v14H2z M2 5l10 8 10-8" fill="var(--blue-deep)" stroke="var(--paper)" stroke-width="1.5"/></svg>
        hello@brisknest.com
      </li>
    </ul>

    <div class="wordmark"><span class="wordmark__square"></span>Brisknest</div>
  </section>

</main>
</body>
</html>
```